Custom Home Builder Needs a Website

Harbor Pine Builders Ltd. requires a clean professional 5 page website - Home, About Us, Gallery (Interior and Exterior), Our Process and Contact Us(with registration form). We are a home builder who also has homes for sale. Also please have a place for video embedding. Editable fields by user. Using the stationery 'feel' that is attached. Need social media links. If you require any additional files, please request.

Target Market(s)

Families and professionals

Industry/Entity Type

Home Builder

Coding

Coded - Design and coding required

Number of Pages Required

5+ page

Font styles to use
Sans Serif
Other font styles liked:
• Lato

Requirements
Must have
• Editable by user
• Register Button
• Place to put home models for sale - preferably on the first page
• 5 page website -
• -Home
• -About Us
• -Gallery (Interior and Exterior)
• -Our Process
• -Contact Us.
Nice to have
• Themed similar to current stationery
• place for video embedding
• Try some darker backgrounds
• Change pictures to B/W if works for design
Should not have
• cartoonish type of content

```html
<!DOCTYPE html>
<html lang="en">
<head>
<meta charset="utf-8">
<title>Harbor Pine Builders Ltd.</title>
<link href="https://fonts.googleapis.com/css2?family=Lato:wght@300;400;700;900&display=swap" rel="stylesheet">
<style>
:root{
  --green:#7cb842;
  --green-dark:#4f8f25;
  --green-deep:#3d7419;
  --green-light:#a8d46f;
  --ink:#333a33;
  --muted:#8a8f8a;
  --gray-bg:#efefef;
  --line:#dcdcdc;
  --white:#ffffff;
}
*{box-sizing:border-box;margin:0;padding:0}
html,body{width:1200px;height:2756px;overflow:hidden}
body{font-family:'Lato',sans-serif;color:var(--ink);background:var(--white);position:relative}
.site-header{height:120px;position:relative;background:var(--white)}
.brand{position:absolute;left:50%;top:30px;transform:translateX(-50%);display:flex;align-items:center;gap:14px}
.brand-mark{width:38px;height:38px;background:var(--green)}
.brand-name{font-weight:900;font-size:26px;color:var(--green-dark);letter-spacing:1px}
.call{position:absolute;right:110px;top:36px;text-align:right}
.call small{display:block;font-size:11px;color:var(--muted);letter-spacing:1px}
.call strong{font-size:24px;color:var(--ink);display:flex;align-items:center;gap:8px}
.main-nav{height:56px;background:linear-gradient(var(--green-light),var(--green));display:flex;padding-left:160px}
.main-nav a{display:block;height:56px;line-height:56px;color:var(--white);text-decoration:none;font-size:16px;font-weight:700;letter-spacing:.5px;text-align:center}
.main-nav a.active{background:#3a3f3a;width:100px}
.hero{height:524px;position:relative;background:linear-gradient(180deg,#9aa3a8 0%,#6e767a 45%,#4d4a44 100%)}
.hero h1{position:absolute;left:120px;top:380px;transform:translateY(-280px);color:var(--white);font-weight:900;font-size:54px;line-height:60px;letter-spacing:1px}
.hero-dots{position:absolute;left:122px;top:232px;display:flex;gap:10px}
.hero-dots span{width:12px;height:12px;border-radius:50%;background:rgba(255,255,255,.6)}
.hero-dots span:first-child{background:var(--white)}
.services{height:340px;display:flex;justify-content:center;gap:70px;padding-top:0}
.service{width:260px;text-align:center;position:relative}
.service-icon{width:140px;height:140px;margin:-4px auto 0;border-radius:50%;background:var(--green);border:8px solid #dceccb;display:flex;align-items:center;justify-content:center}
.service h3{margin-top:14px;font-size:20px;color:var(--green-dark);font-weight:700}
.service p{margin-top:10px;font-size:13px;line-height:20px;color:var(--muted)}
.btn{display:inline-block;background:var(--green-dark);color:var(--white);font-size:12px;font-weight:700;padding:8px 22px;margin-top:16px;text-decoration:none}
.about{height:420px;background:var(--gray-bg);position:relative;padding:0 120px}
.about-text{position:absolute;left:120px;top:70px;width:520px}
.about h2{font-size:32px;font-weight:400;color:var(--ink)}
.about p{font-size:14px;line-height:22px;color:var(--muted);margin-top:18px}
.btn-outline{display:inline-block;border:2px solid var(--green);color:var(--green-dark);font-size:13px;font-weight:700;padding:10px 20px;margin-top:24px}
.video{position:absolute;left:720px;top:96px;width:352px;height:224px;background:linear-gradient(180deg,#c8cdd2,#6a6f6c 70%,#3e4a36);display:flex;align-items:center;justify-content:center}
.play{width:68px;height:68px;border-radius:50%;background:var(--white);display:flex;align-items:center;justify-content:center}
.about-edge{position:absolute;left:0;bottom:-40px;width:1200px;height:40px}
.section-title{text-align:center;font-size:38px;font-weight:400;color:var(--ink)}
.gallery{padding-top:100px}
.gallery-strip{display:flex;margin-top:30px;height:248px}
.gallery-strip div{flex:1;position:relative;display:flex;align-items:center;justify-content:center}
.g1{background:linear-gradient(#b9c3c9,#5a6d44)}
.g2{background:linear-gradient(#8d9499,#4d5650)}
.g3{background:linear-gradient(#e3e6e8,#a7acab)}
.g4{background:linear-gradient(#d8d1c4,#6d5845)}
.g5{background:linear-gradient(#8a7260,#3e2f25)}
.zoom{width:44px;height:44px;border-radius:50%;background:rgba(255,255,255,.85);display:flex;align-items:center;justify-content:center}
.sales{padding-top:70px}
.cards{display:flex;gap:16px;justify-content:center;margin-top:30px}
.card{width:310px;height:400px;border:1px solid var(--line);text-align:center;background:var(--white)}
.card-photo{height:208px}
.c1{background:linear-gradient(#c7d1d8,#6f7a66)}
.c2{background:linear-gradient(#aeb8c0,#5d6b52)}
.c3{background:linear-gradient(#9da5ab,#4f5750)}
.card h4{font-size:16px;font-weight:700;margin-top:30px}
.card p{font-size:12px;color:var(--muted);line-height:18px;margin:10px 30px 0}
.card a{display:inline-block;margin-top:14px;font-size:12px;font-weight:700;color:var(--green-dark);text-decoration:none}
.site-footer{position:absolute;left:0;top:2400px;width:1200px;height:356px;background:linear-gradient(180deg,var(--green-light),var(--green) 60%,var(--green-dark))}
.footer-col{position:absolute;top:62px;color:var(--white)}
.footer-col h5{font-size:22px;font-weight:400;margin-bottom:16px}
.footer-col li{list-style:none;font-size:14px;line-height:24px}
.social{display:flex;gap:8px;margin-top:12px}
.social span{width:26px;height:26px;border-radius:50%;border:2px solid var(--white)}
.copyright{position:absolute;bottom:22px;width:100%;text-align:center;font-size:12px;color:var(--white)}
</style>
</head>
<body>
<header class="site-header">
  <div class="brand"><span class="brand-mark"></span><span class="brand-name">Harbor Pine Builders Ltd.</span></div>
  <div class="call"><small>CALL US NOW</small><strong>
    <svg width="20" height="20" viewBox="0 0 24 24"><path fill="#7cb842" d="M6.6 10.8a15.1 15.1 0 006.6 6.6l2.2-2.2a1 1 0 011-.25 11.4 11.4 0 003.6.6 1 1 0 011 1V20a1 1 0 01-1 1A17 17 0 013 4a1 1 0 011-1h3.5a1 1 0 011 1c0 1.25.2 2.45.6 3.6a1 1 0 01-.25 1z"/></svg>
    (555) 014 2270</strong></div>
</header>
<nav class="main-nav">
  <a class="active" href="#">HOME</a>
  <a href="#" style="width:180px;margin-left:40px">ABOUT US</a>
  <a href="#" style="width:180px">GALLERY</a>
  <a href="#" style="width:220px">OUR PROCESS</a>
  <a href="#" style="width:200px">CONTACT US</a>
</nav>
<section class="hero" role="img" aria-label="Photo of a newly built two-storey home with a double garage">
  <h1>EXTERIOR &amp; INTERIOR<br>CONSTRUCTION</h1>
  <div class="hero-dots"><span></span><span></span><span></span><span></span></div>
</section>
<section class="services">
  <div class="service">
    <div class="service-icon"><svg width="60" height="60" viewBox="0 0 60 60" fill="none" stroke="#fff" stroke-width="3"><rect x="8" y="8" width="44" height="44"/><path d="M8 30h22V8M30 30v22"/></svg></div>
    <h3>INTERIOR DESIGN</h3>
    <p>Thoughtful layouts and finishes chosen to suit the way your family lives every day.</p>
    <a class="btn" href="#">LEARN MORE</a>
  </div>
  <div class="service">
    <div class="service-icon"><svg width="60" height="60" viewBox="0 0 60 60" fill="none" stroke="#fff" stroke-width="3"><rect x="10" y="10" width="40" height="40"/><path d="M30 10v40M10 30h40"/></svg></div>
    <h3>EXTERIOR DESIGN</h3>
    <p>Durable facades and rooflines crafted to stand out and stand up to every season.</p>
    <a class="btn" href="#">LEARN MORE</a>
  </div>
  <div class="service">
    <div class="service-icon"><svg width="60" height="60" viewBox="0 0 60 60" fill="none" stroke="#fff" stroke-width="3"><path d="M8 28L30 8l22 20M14 24v28h32V24"/><text x="30" y="45" fill="#fff" stroke="none" font-family="Lato,sans-serif" font-size="18" font-weight="700" text-anchor="middle">$</text></svg></div>
    <h3>SELLING HOME</h3>
    <p>Browse move-in ready homes built with care and ready for your family today.</p>
    <a class="btn" href="#">LEARN MORE</a>
  </div>
</section>
<section class="about">
  <div class="about-text">
    <h2>About Harbor Pine Builders Ltd.</h2>
    <p>Every home we build starts with a conversation about how you want to live, work and grow together.</p>
    <p>From the first sketch to the final walkthrough our team handles each detail so your new home feels right the day you arrive.</p>
    <span class="btn-outline">LEARN MORE</span>
  </div>
  <div class="video" role="img" aria-label="Video preview showing a finished family home">
    <div class="play"><svg width="26" height="26" viewBox="0 0 26 26"><path d="M8 4l14 9-14 9z" fill="#333a33"/></svg></div>
  </div>
  <svg class="about-edge" viewBox="0 0 1200 40" preserveAspectRatio="none"><path d="M0 0h1200v6L600 40 0 6z" fill="#efefef"/></svg>
</section>
<section class="gallery">
  <h2 class="section-title">Our Gallery</h2>
  <div class="gallery-strip">
    <div class="g1" role="img" aria-label="Exterior of a home with lawn"></div>
    <div class="g2" role="img" aria-label="Front view of a two-storey home"><span class="zoom"><svg width="20" height="20" viewBox="0 0 20 20" fill="none" stroke="#333a33" stroke-width="2"><circle cx="8" cy="8" r="6"/><path d="M13 13l5 5"/></svg></span></div>
    <div class="g3" role="img" aria-label="Bright white kitchen interior"></div>
    <div class="g4" role="img" aria-label="Living room interior"></div>
    <div class="g5" role="img" aria-label="Kitchen with dark wood cabinets"></div>
  </div>
</section>
<section class="sales">
  <h2 class="section-title">Home for Sales</h2>
  <div class="cards">
    <article class="card"><div class="card-photo c1" role="img" aria-label="Home for sale with gabled roof"></div><h4>Home Tittle here</h4><p>Four bedrooms, two baths and a bright open kitchen.</p><a href="#">VIEW MORE</a></article>
    <article class="card"><div class="card-photo c2" role="img" aria-label="Home for sale with front porch"></div><h4>Home Tittle here</h4><p>Three bedrooms with a double garage and large yard.</p><a href="#">VIEW MORE</a></article>
    <article class="card"><div class="card-photo c3" role="img" aria-label="Home for sale on a quiet street"></div><h4>Home Tittle here</h4><p>Modern family home close to parks and local schools.</p><a href="#">VIEW MORE</a></article>
  </div>
</section>
<footer class="site-footer">
  <div class="footer-col" style="left:136px"><h5>Company</h5><ul><li>Home</li><li>About Us</li><li>Gallery</li><li>Our Process</li></ul></div>
  <div class="footer-col" style="left:368px"><h5>Resources</h5><ul><li>Blogs</li><li>Testimonials</li><li>Recent Projects</li><li>News</li></ul></div>
  <div class="footer-col" style="left:612px"><h5>Legal</h5><ul><li>Term of use</li><li>Privacy Policy</li><li>Contact Us</li></ul></div>
  <div class="footer-col" style="left:792px"><h5>Contact Us</h5><ul><li>1420 Cedar Ridge Road Suite 12</li><li>Fairhaven, WA 98225</li><li>(555) 014 2270</li><li>hello@harborpinebuilders.com</li></ul>
    <div class="social"><span></span><span></span><span></span><span></span></div></div>
  <p class="copyright">© 2016 Harbor Pine Builders Ltd. All rights reserved.</p>
</footer>
</body>
</html>
```